Format a newsletter

We have developed a 4 page word document as part of a newsletter and brochure that we will email (PDF) and post (printed copy) to clients and colleagues.

The current document is quite bland and could be made to look more professional.

The new format should look professionally presented and work in print and PDF format.
Updates

Please note additional comments: 1) I have uploaded PDF of logos 2) Please ensure that a Word version of the final design is provided as we will likely update some text before printing 3) A little background on Brimholt and the target audience f this communication: Brimholt is a corporate advisory company with a 30 year history. We assist with mergers and acquisitions and typically support small to medium sized companies. Our intended audience are accountants, lawyers, bankers, consultants and business owners. Our market positioning is: professional, integrity, sophisticated but approachable. Our greatest competitors are tier 1 and tier 2 accounting firms.

Designers I'm not sure whether the 4 page Word document that needs to be formatted uploaded correctly when the project was posted. I have re-uploaded the Word document. Thankyou

Please note that the document that needs to be formatted is the 4 page Word document: "Brimholt predictions for M&A 2015v2 ext". Thanks

Reason: Am giving time for more creative designs

Target Market(s)

Accountants, lawyers, bankers and business owners

Industry/Entity Type

Work

Requirements
Nice to have
• 1) Ideally print as a 4 page folded brochure (not critical)
2) Have uploaded our corporate colours: Cosmic Blue (R 21, G 51, B 74) or (C 94, M 75, Y 46 K43) and White
Should not have
• Tacky cartoons or cartoons

```html
<!DOCTYPE html>
<html lang="en">
<head>
<meta charset="utf-8">
<title>Implications for the SME Owner – Brimholt</title>
<link rel="stylesheet" href="https://fonts.googleapis.com/css2?family=Open+Sans:ital,wght@0,300;0,400;0,600;0,700;1,400&display=swap">
<style>
:root{
  --cosmic:#15334a;
  --cosmic-deep:#0f2436;
  --sky:#3f6f9a;
  --sky-light:#a9c3da;
  --paper:#ffffff;
  --ink:#3a3a3a;
  --rule:#c9d3dc;
  --backdrop:#8a8a8a;
}
*{box-sizing:border-box;margin:0;padding:0}
html,body{width:1200px;height:800px;overflow:hidden}
body{background:var(--backdrop);font-family:"Open Sans",sans-serif;color:var(--ink)}
.spread{position:absolute;left:30px;top:10px;width:1140px;height:780px;display:flex;box-shadow:0 6px 24px rgba(0,0,0,.35)}
.page{position:relative;width:570px;height:780px;background:var(--paper);overflow:hidden}
.page--left{border-right:1px solid #e2e2e2}
.masthead{position:absolute;left:0;top:0;width:100%;height:165px;
  background:linear-gradient(160deg,var(--sky-light) 0%,var(--sky) 35%,var(--cosmic) 75%,var(--cosmic-deep) 100%)}
.masthead__contact{position:absolute;right:22px;top:22px;text-align:right;color:#fff;font-size:8px;line-height:1.9}
.title-bar{position:absolute;left:0;top:130px;width:100%;height:35px;background:var(--cosmic);display:flex;align-items:center;padding-left:26px;border-top:1px solid rgba(255,255,255,.35)}
.title-bar h1{font-weight:400;font-size:15px;color:#fff;letter-spacing:.2px}
.body{position:absolute;left:30px;right:30px;top:186px;bottom:80px;font-size:8.3px;line-height:1.36}
.columns{display:flex;gap:22px;height:100%}
.col{flex:1}
.body p{margin-bottom:8px}
.body h2{font-size:9px;font-weight:700;color:var(--cosmic);margin-bottom:2px}
.point{display:flex;gap:6px;margin-bottom:4px}
.point__num{font-weight:700;color:var(--cosmic);font-size:9px}
.dash-list{list-style:none;margin-bottom:8px}
.dash-list li{padding-left:9px;position:relative}
.dash-list li::before{content:"-";position:absolute;left:0}
.contact h3{font-size:8.3px;font-weight:700;color:var(--cosmic);margin:8px 0 10px}
.contact p{margin-bottom:12px}
.contact b{font-weight:700}
.matches{position:absolute;left:50px;right:40px;top:470px;height:110px;
  background:radial-gradient(ellipse at 50% 55%,#d9c08a 0%,#c9a867 28%,#f1efea 62%,#ffffff 100%)}
.footer-line{position:absolute;left:150px;right:30px;bottom:64px;border-top:1px solid var(--rule)}
.confidential{position:absolute;right:32px;bottom:46px;font-style:italic;font-size:10.5px;color:var(--cosmic)}
.footer-band{position:absolute;left:0;right:0;bottom:0;height:40px;background:var(--cosmic)}
.brand{position:absolute;display:flex;align-items:center;gap:6px;font-weight:300;font-size:19px;letter-spacing:1px}
.brand__mark{width:12px;height:12px}
.page--left .brand{left:28px;bottom:9px;color:#fff}
.page--left .brand__mark{background:#fff}
.page--right .brand{left:28px;bottom:48px;color:var(--cosmic)}
.page--right .brand__mark{background:var(--cosmic)}
.page--right .footer-band{left:260px;height:28px}
.page--right .confidential{bottom:6px;color:#fff}
.page--right .footer-line{left:200px;bottom:40px}
.page--right .body{top:200px;left:50px;right:auto;width:290px}
.page--right .body > p{padding-left:14px}
</style>
</head>
<body>
<div class="spread">

  <section class="page page--left">
    <div class="masthead" role="img" aria-label="Photograph of blue jigsaw puzzle pieces being joined">
      <div class="masthead__contact">T +61 7 3555 0142 &nbsp; E info@brimholt.com.au<br>Harlow Capital AFSL 612907<br>Brimholt Business &nbsp;·&nbsp; Brimholt Victoria</div>
    </div>
    <div class="title-bar"><h1>Implications for the SME Owner</h1></div>

    <div class="body">
      <div class="columns">
        <div class="col">
          <p>To best respond to these emerging M&amp;A trends for SMEs, Brimholt believes there are three important considerations for owners and their advisers:</p>
          <div class="point"><span class="point__num">1.</span><div>
            <h2>Prepare the business for sale</h2>
            <p>At least 6 to 12 months prior to the commencement of a sale process, business owners and their advisers should clinically assess the attractiveness of the business to potential buyers. They need to consider the important characteristics that buyers will value, such as the independence of the business from the current owners, the extent to which revenues are contracted, barriers to competition and the earnings trend of the business.</p>
            <p>It is then critical that the owner and their adviser commence development of the “data room” by capturing key financial, legal and commercial information regarding the business. Once the business is under offer and a prospective buyer commences due diligence, ensuring the data is readily available will assist to maintain momentum and reduce the likelihood of renegotiation or the deal collapsing entirely.</p>
            <p>As a simple example, the inability to justify earnings normalisations (“add-backs”) can lead to the collapse of a contract which could cost seller and buyers tens of thousands of dollars in professional fees as well as the loss of several months invested in the sale campaign.</p>
          </div></div>
          <div class="point"><span class="point__num">2.</span><div>
            <h2>Plan for a sophisticated sale process</h2>
            <p>Many small businesses worth less than $1 million are sold by business brokers using traditional reactive marketing channels such as web advertising. With the increasing volume of SMEs available for sale, competition amongst the SMEs to attract buyers will intensify.</p>
            <p>Business owners who are seeking to exit for an optimal outcome will need to employ sophisticated sale campaigns to generate greater awareness and highlight the specific benefits of their business.</p>
          </div></div>
        </div>
        <div class="col">
          <p style="margin-bottom:2px">To be successful, sale campaigns may include:</p>
          <ul class="dash-list">
            <li>Direct approach to industry buyers through a competitive expression of interest program detailing the strategic advantages of the acquisition of the SME.</li>
            <li>Rigorous financial analysis that will support credible marketing to private equity and family office targets as a financial investment.</li>
            <li>Modelling of a leveraged buy-out with the payment of fully-franked dividends to attract investment syndicates.</li>
            <li>Promotion to international trade and financial buyers with appropriate professional support to enable them to efficiently enter the Australian market.</li>
            <li>Marketing to Asian buyers with support to assist with their visa applications (where applicable).</li>
            <li>Merger or roll-up with other SMEs within the same industry, adjacent industry or within the supply chain (i.e. vertical integration) as a transitionary step to complete exit.</li>
          </ul>
          <div class="point"><span class="point__num">3.</span><div>
            <h2>Access capable M&amp;A advisory expertise with demonstrable ROI</h2>
            <p>Owners who are planning to divest should ensure they have adequate expertise to properly prepare the business for sale. This requires experience in both the sell side and buy side of SMEs to understand what trade buyers, financial buyers and individuals will look for when they assess the business.</p>
            <p>Owners who are considering acquisitions must plan for the acquisition, negotiation and completion of the transaction. As importantly, they must be equipped to complete the post-merger integration of the acquisition to ensure synergies are harvested and the acquisition delivers the benefits that were modelled prior to the transaction.</p>
            <p>Most SME owners will engage advisers such as their accountants, lawyers, M&amp;A professionals and/or corporate advisers to assist them with the M&amp;A process. In doing so, the owners should ensure their advisers have the relevant experience with comparable transactions. Importantly, owners should engage</p>
          </div></div>
        </div>
      </div>
    </div>

    <div class="footer-line"></div>
    <div class="confidential">Commercial in Confidence</div>
    <div class="footer-band"></div>
    <div class="brand"><span class="brand__mark"></span>BRIMHOLT</div>
  </section>

  <section class="page page--right">
    <div class="masthead" role="img" aria-label="Photograph of blue jigsaw puzzle pieces being joined">
      <div class="masthead__contact">T +61 7 3555 0142 &nbsp; E info@brimholt.com.au<br>Harlow Capital AFSL 612907<br>Brimholt Business &nbsp;·&nbsp; Brimholt Victoria</div>
    </div>
    <div class="title-bar"><h1>Implications for the SME Owner</h1></div>

    <div class="body">
      <p>advisers with some element of remuneration based on outcome. This will enhance the alignment of interests between the SME owner and their adviser. Importantly, it will enable the owner to measure the tangible return on investment they receive from their advisory fees.</p>
      <div class="contact">
        <h3>For more information contact:</h3>
        <p>Daniel Verhoef - Director Harlow Capital<br><b>E:</b> daniel.verhoef@brimholt.com.au<br><b>T:</b> (07) 3555 0142</p>
        <p>Owen Castell - Director Brimholt (Victoria)<br><b>E:</b> owen.castell@brimholt.com.au<br><b>T:</b> (03) 9555 0187</p>
      </div>
    </div>

    <div class="matches" role="img" aria-label="Photograph of a row of burnt matches with one unlit red match in the middle"></div>

    <div class="footer-line"></div>
    <div class="brand"><span class="brand__mark"></span>BRIMHOLT</div>
    <div class="footer-band"></div>
    <div class="confidential">Commercial in Confidence</div>
  </section>

</div>
</body>
</html>
```